Italian Made to Measure Menswear Business needs a brochure to promote my services

I need a brochure that promotes my Italian Made-to-Measure Menswear business. The brochure should be in line with the style of my logo (attached) and my website is lucafiore.com

I'd like to highlight part of the brochure the promotion of buy one MTM suit and get one FREE MTM dress shirt.

I'd like to also make sure potential clients understand that I can go to their offices or they can come to my showroom.

Contact info should also be visible in the brochure:

DARIO VENTI
872 W. Heron Bay Ave.
Suite 410
Boca Raton, FL 33517
Tel. 561-847-2163

The final design should be classy and communicate a sense of style, along with inviting people to look good.
Updates

Hello Designers, Please also make sure that: - The front of the brochure should highlight what I do: Italian Made to Measure and Ready to Wear Menswear - I need to advertise the buy one Made to Measure suit and get one FREE dress shirt ($175 value) - Please use terms like STYLE, ITALIAN, EXCLUSIVE, ELEGANCE, PRESTIGIOUS, STYLISH, CLASSY, LUXURY - make sure the brochure is mostly about the potential client (YOU... YOURS...) - Less highlighted but somewhere to make sure the message of luxury doesn't scare people with smaller budgets: AFFORDABLE ELEGANCE or similar Thanks!

PLEASE NOTE SOME OF THE TEXT ON THE WEBSITE HAS CHANGED. ALSO FEEL FREE TO GO ON OUR FACEBOOK PAGE AS WELL TO GET INSPIRED. This should be the main presentation line: Dario Venti is an Italian Custom Clothier that offers one-on-one service to gentlemen in South Florida. Luxury menswear and 24/7 assistance for everyone. Thank you everyone for your great efforts!!

Target Market(s)

Sophisticated gentlemen in search of improving their looks and that are conscious about the importance of getting well dressed.

Industry/Entity Type

Business

Requirements
Must have
• Two page, bi-folded or tri-folded brochure. Please use the pictures provided, the ones on my website or get them on your own as long as they reflect the actual business (detailed pictures).

Must feature a promotion buy one MTM suit and get one FREE MTM dress shirt.
Nice to have
• As far as style - should be in line with my business card (attached). Doesn't have to match exactly but would be nice if it didn't go to far away from it.
Should not have
• Too bright colors

```html
<!DOCTYPE html>
<html lang="en">
<head>
<meta charset="utf-8">
<title>Dario Venti – Brochure</title>
<link rel="stylesheet" href="https://fonts.googleapis.com/css2?family=Crimson+Text:ital,wght@0,400;0,600;0,700;1,400&display=swap">
<style>
  :root {
    --backdrop: #7a5a3a;
    --slate: #3b3e43;
    --slate-dark: #303337;
    --slate-light: #4a4e54;
    --ink-light: #e6e6e6;
    --ink-soft: #c9cbce;
    --box-grey: #b9bbbe;
    --heading-dark: #3a3c40;
    --italian-green: #2f9a3e;
    --italian-red: #c8262a;
    --photo-light: #9a9a9a;
    --photo-dark: #3c3c3c;
  }
  * { box-sizing: border-box; margin: 0; padding: 0; }
  html, body { width: 1200px; height: 626px; overflow: hidden; }
  body {
    background: var(--backdrop);
    font-family: "Crimson Text", Georgia, serif;
    position: relative;
  }
  .brochure {
    position: absolute;
    left: 208px; top: 33px;
    width: 785px; height: 560px;
    background: linear-gradient(90deg, var(--slate-dark), var(--slate) 30%, var(--slate-light) 50%, var(--slate) 75%, var(--slate-dark));
    box-shadow: 0 6px 18px rgba(0,0,0,0.35);
    overflow: hidden;
  }
  .panel { position: absolute; top: 0; height: 100%; }
  .panel--inside { left: 0; width: 266px; }
  .panel--back {
    left: 266px; width: 245px;
    background: linear-gradient(90deg, rgba(255,255,255,0.02), rgba(255,255,255,0.09) 55%, rgba(255,255,255,0.03));
  }
  .panel--front { left: 511px; width: 274px; }

  .edge-stripe { position: absolute; left: 14px; top: 0; width: 4px; height: 100%; background: var(--ink-soft); opacity: 0.55; }

  .section-title {
    position: absolute; left: 23px; top: 26px; width: 218px; height: 72px;
    background: var(--box-grey);
    color: var(--heading-dark);
    font-size: 30px; line-height: 30px; letter-spacing: 0.5px; font-weight: 400;
    font-variant: small-caps; padding: 6px 0 0 10px;
  }
  .accent { position: absolute; height: 5px; }
  .accent--green { background: var(--italian-green); }
  .accent--red { background: var(--italian-red); }

  .feature { position: absolute; left: 28px; width: 230px; color: var(--ink-light); }
  .feature h2 { font-size: 21px; font-weight: 600; line-height: 24px; margin-bottom: 1px; }
  .feature p { font-size: 13.6px; line-height: 16.4px; text-align: justify; color: var(--ink-soft); }
  .feature--service { top: 136px; }
  .feature--art { top: 334px; }

  .photo {
    position: absolute; left: 266px; top: 110px; width: 519px; height: 304px;
    background: linear-gradient(135deg, var(--photo-light) 0%, #7d7d7d 40%, #5a5a5a 70%, var(--photo-dark) 100%);
  }

  .promo {
    position: absolute; left: 14px; top: 22px; width: 217px;
    text-align: center; color: var(--ink-light);
  }
  .promo-lead { display: block; font-size: 13px; line-height: 16px; letter-spacing: 1.5px; color: var(--ink-soft); }
  .promo-main { display: block; font-size: 17px; line-height: 20px; font-weight: 600; }
  .promo-note { display: block; font-size: 13px; line-height: 16px; color: var(--ink-soft); }

  .brand-name {
    color: var(--ink-soft); font-weight: 400; font-style: normal; letter-spacing: 4px;
    text-align: center; white-space: nowrap;
  }
  .brand-name--front { position: absolute; left: 0; width: 274px; top: 38px; font-size: 34px; }
  .brand-name--back { font-size: 18px; letter-spacing: 2px; margin-bottom: 10px; }

  .contact {
    position: absolute; left: 0; top: 430px; width: 245px;
    text-align: center; color: var(--ink-soft); font-style: normal;
    font-size: 13px; line-height: 15px;
  }
  .contact-line { display: flex; justify-content: center; gap: 5px; margin-bottom: 9px; }
  .contact-line svg { flex: none; margin-top: 2px; fill: var(--ink-soft); }

  .tagline { position: absolute; right: 17px; top: 466px; text-align: right; color: var(--ink-light); }
  .tagline-lead { font-size: 20px; line-height: 24px; }
  .tagline-main { font-size: 27px; line-height: 30px; font-weight: 700; }
</style>
</head>
<body>
  <main class="brochure">
    <section class="panel panel--inside">
      <div class="edge-stripe"></div>
      <div class="accent accent--green" style="left:143px; top:20px; width:98px;"></div>
      <h1 class="section-title">Service and<br>Products</h1>
      <div class="accent accent--red" style="left:23px; top:98px; width:93px;"></div>

      <article class="feature feature--service">
        <h2>Impeccable Service</h2>
        <p>We are proud to be considered the best service of this kind in South Florida by our clients. Give us a call and set an appointment with us to better understand how we built this reputation. We come to your office or home, at your convenience. No need to get in the car or see where the closest menswear store is.</p>
      </article>

      <article class="feature feature--art">
        <h2>State of the Art</h2>
        <p>Whether it's a suit or just a sport jacket, a pair of trousers or a dress shirt, our final product is a Masterpiece; a combination of State of the Art sartorial craftsmanship and luxurious Italian fabrics. A Masterpiece designed around your body.</p>
      </article>
    </section>

    <div class="accent accent--green" style="left:266px; top:104px; width:353px; height:8px;"></div>
    <div class="photo" role="img" aria-label="Black and white photo of a tailor's hands marking the shoulder of a grey suit jacket with chalk"></div>
    <div class="accent accent--red" style="left:443px; top:410px; width:342px; height:7px;"></div>

    <section class="panel panel--back">
      <p class="promo">
        <span class="promo-lead">BUY ONE MADE TO MEASURE SUIT</span>
        <span class="promo-main">Get one FREE dress shirt</span>
        <span class="promo-note">($175 value)</span>
      </p>
      <address class="contact">
        <div class="brand-name brand-name--back">DARIO VENTI</div>
        <div class="contact-line">
          <svg width="9" height="12" viewBox="0 0 9 12"><path d="M4.5 0A4.5 4.5 0 0 0 0 4.5C0 8 4.5 12 4.5 12S9 8 9 4.5A4.5 4.5 0 0 0 4.5 0zm0 6.3a1.8 1.8 0 1 1 0-3.6 1.8 1.8 0 0 1 0 3.6z"/></svg>
          <span>872 West Heron Bay Avenue,<br>Suite 410, Boca Raton, FL,<br>United States</span>
        </div>
        <div class="contact-line">
          <svg width="11" height="11" viewBox="0 0 24 24"><path d="M6.6 10.8a15.1 15.1 0 0 0 6.6 6.6l2.2-2.2c.3-.3.7-.4 1-.2 1.1.4 2.3.6 3.6.6.6 0 1 .4 1 1V20c0 .6-.4 1-1 1A17 17 0 0 1 3 4c0-.6.4-1 1-1h3.5c.6 0 1 .4 1 1 0 1.3.2 2.5.6 3.6.1.3 0 .7-.2 1z"/></svg>
          <span>+1.5618472163</span>
        </div>
        <div class="contact-line">
          <svg width="12" height="9" viewBox="0 0 12 9"><path d="M0 0h12v9H0z" opacity="0.9"/><path d="M0 0l6 5 6-5" fill="none" stroke="#3b3e43" stroke-width="1"/></svg>
          <span>dario@lucafiore.com</span>
        </div>
      </address>
    </section>

    <section class="panel panel--front">
      <div class="brand-name brand-name--front">DARIO VENTI</div>
      <p class="tagline">
        <span class="tagline-lead">Don't compromise on</span><br>
        <span class="tagline-main">Personal Elegance</span>
      </p>
    </section>
  </main>
</body>
</html>
```